Chicago Train Advertisement for HomeAlongRail.com.

We have purchased one month of advertising on the Chicago NRX subway train. We will have 150 cards up in the subway to advertise our website HomeAlongRail.com where people can search for properties by train station. The cards are 11" tall and 46.5" long. We want people to feel compelled to jump on their cell phones and conduct a search for an apartment or home while they are riding the train, or at least enter their email and search criteria so one of our agents can help them.

Target Market(s)

People who want to live near train stations

Industry/Entity Type

Real Estate

Font styles to use
Sans Serif

Colors

Designer to choose colors to be used in the design.

Requirements
Must have
• The homealongrail logo and a catchy slogan, something like: Find your home near a train station the easy way: www.homealongral.com. Search real estate listings near the NRX or Velco.

```html
<!DOCTYPE html>
<html lang="en">
<head>
<meta charset="utf-8">
<title>HomeAlongRail.com — Train Card</title>
<link rel="stylesheet" href="https://fonts.googleapis.com/css2?family=Roboto:wght@300;400;500&display=swap">
<style>
  :root {
    --sky: #3fa9de;
    --sky-deep: #2b93cf;
    --ink: #2a2a2a;
    --navy: #272b4a;
    --paper: #ffffff;
  }
  html, body {
    margin: 0;
    padding: 0;
    overflow: hidden;
    background: var(--paper);
  }
  .train-card {
    position: relative;
    width: 1200px;
    height: 284px;
    background: var(--paper);
    overflow: hidden;
    font-family: "Roboto", Arial, sans-serif;
  }
  .headline {
    position: absolute;
    left: 56px;
    top: 58px;
    margin: 0;
    font-weight: 300;
    font-size: 49px;
    line-height: 61px;
    letter-spacing: 0.5px;
    color: var(--sky);
    text-transform: uppercase;
  }
  .headline .line { display: block; white-space: nowrap; }
  .headline .pun {
    font-weight: 400;
    color: var(--sky-deep);
  }
  .search-note {
    position: absolute;
    left: 490px;
    top: 190px;
    margin: 0;
    font-size: 16.5px;
    line-height: 22px;
    font-weight: 400;
    color: var(--ink);
  }
  .brand {
    position: absolute;
    left: 846px;
    top: 160px;
    display: flex;
    align-items: center;
    gap: 10px;
  }
  .brand-dot {
    width: 26px;
    height: 26px;
    border-radius: 50%;
    background: var(--sky);
  }
  .brand-name {
    font-size: 24px;
    font-weight: 500;
    color: var(--navy);
    letter-spacing: -0.3px;
  }
  .web-address {
    position: absolute;
    left: 811px;
    top: 228px;
    margin: 0;
    font-size: 29px;
    font-weight: 400;
    color: var(--ink);
  }
</style>
</head>
<body>
  <main class="train-card">
    <h1 class="headline">
      <span class="line">Everything so close,</span>
      <span class="line">You”ll find life</span>
      <span class="line">Enter<span class="pun">train</span>ing.</span>
    </h1>
    <p class="search-note">Search real estate listings<br>near the NRX or Velco.</p>
    <div class="brand">
      <span class="brand-dot" aria-hidden="true"></span>
      <span class="brand-name">HomeAlongRail.com</span>
    </div>
    <p class="web-address">www.homealongral.com.</p>
  </main>
</body>
</html>
```